Tidewell Electrical Solutions

On one side. LOGO (underneath:) Commercial Industrial Residential

- NAME & CONTACT DETAILS

Martin K. Oduya
Project Manager

(Cell icon) (441) 555-0187
(Email icon) twlelectricalsoultions@mailpost-demo.com
(Facebook & Instagram icons )@twlelectricalsolutions

Other side: LOGO - underneath ELECTRICAL CONSTRUCTION & MAINTENANCE . LED LIGHTING & AUTOMATION . LIFE SAFETY SYSTEMS (FIRE ALARM / SECURITY) . DATA & COMMUNICATION

```html
<!DOCTYPE html>
<html lang="en">
<head>
<meta charset="utf-8">
<title>Tidewell Electrical Solutions — Business Card</title>
<link rel="stylesheet" href="https://fonts.googleapis.com/css2?family=Montserrat:wght@400;500;600&display=swap">
<style>
  :root {
    --teal: #105a6e;
    --teal-deep: #0f5468;
    --white: #ffffff;
    --ink-grey: #3c3c3c;
    --page: #e9e5de;
  }
  * { margin: 0; padding: 0; box-sizing: border-box; }
  html, body {
    width: 1200px; height: 900px; overflow: hidden;
    background: var(--page);
    font-family: "Montserrat", Arial, sans-serif;
  }
  .canvas { position: relative; width: 1200px; height: 900px; }
  .card {
    position: absolute; left: 311px; width: 577px; height: 329px;
  }
  .card--front { top: 98px; background: var(--teal); color: var(--white); }
  .card--back { top: 472px; background: var(--white); color: var(--teal); }

  /* wordmark */
  .wordmark { position: absolute; display: flex; align-items: center; gap: 12px; }
  .wordmark__square { width: 26px; height: 26px; }
  .wordmark__name {
    font-weight: 500; font-size: 15px; line-height: 1.05;
    letter-spacing: 1.6px; text-transform: uppercase;
  }
  .card--front .wordmark { left: 0; right: 0; top: 132px; justify-content: center; }
  .card--front .wordmark__square { background: var(--white); }
  .card--front .wordmark__name { color: var(--white); }
  .card--back .wordmark { left: 30px; top: 42px; }
  .card--back .wordmark__square { background: var(--teal); }
  .card--back .wordmark__name { color: var(--teal); }

  .services {
    position: absolute; left: 0; right: 0; top: 262px;
    text-align: center; font-size: 13px; font-weight: 500;
    letter-spacing: 0.6px; line-height: 15.5px; text-transform: uppercase;
  }

  .person { position: absolute; right: 33px; top: 170px; text-align: right; }
  .person__title { font-size: 13px; color: var(--ink-grey); line-height: 16px; }
  .person__name { font-size: 17px; font-weight: 500; color: var(--teal); line-height: 20px; }

  .sectors {
    position: absolute; left: 30px; right: 36px; top: 210px;
    display: flex; align-items: center; gap: 6px;
    font-size: 13px; font-weight: 500; color: var(--teal);
  }
  .sectors__rule { flex: 1; height: 2px; background: var(--teal); }

  .contact { position: absolute; left: 30px; font-size: 13.5px; color: var(--ink-grey); display: flex; align-items: center; gap: 9px; }
  .contact--phone { top: 241px; }
  .contact--email { top: 264px; font-size: 13px; }
  .contact__icon { width: 18px; height: 18px; flex: none; }

  .social { position: absolute; right: 33px; top: 241px; display: flex; gap: 8px; }
  .social__dot { width: 18px; height: 18px; border-radius: 50%; background: var(--teal); }
  .handle { position: absolute; right: 33px; top: 264px; font-size: 13.5px; color: var(--ink-grey); }
</style>
</head>
<body>
<main class="canvas">
  <section class="card card--front" aria-label="Card front">
    <div class="wordmark">
      <span class="wordmark__square"></span>
      <span class="wordmark__name">Tidewell<br>Electrical<br>Solutions</span>
    </div>
    <p class="services">
      Electrical Construction &amp; Maintenance<br>
      Life Safety Systems (Fire Alarm | Security)<br>
      LED Lighting &amp; Automation &nbsp;|&nbsp; Data &amp; Communication
    </p>
  </section>

  <section class="card card--back" aria-label="Card back">
    <div class="wordmark">
      <span class="wordmark__square"></span>
      <span class="wordmark__name">Tidewell<br>Electrical<br>Solutions</span>
    </div>

    <div class="person">
      <p class="person__title">Project Manager</p>
      <p class="person__name">Martin K. Oduya</p>
    </div>

    <div class="sectors">
      <span>Commercial Industrial Residential</span>
      <span class="sectors__rule"></span>
    </div>

    <p class="contact contact--phone">
      <svg class="contact__icon" viewBox="0 0 18 18" aria-hidden="true">
        <circle cx="9" cy="9" r="9" fill="#105a6e"/>
        <rect x="6" y="3.5" width="6" height="11" rx="1.2" fill="none" stroke="#fff" stroke-width="1.3"/>
        <circle cx="9" cy="12.4" r="0.7" fill="#fff"/>
      </svg>
      (441) 555-0187
    </p>
    <p class="contact contact--email">
      <svg class="contact__icon" viewBox="0 0 18 18" aria-hidden="true">
        <circle cx="9" cy="9" r="9" fill="#105a6e"/>
        <rect x="4.5" y="6" width="9" height="6.5" rx="0.6" fill="#fff"/>
        <path d="M4.8 6.3 L9 9.6 L13.2 6.3" fill="none" stroke="#105a6e" stroke-width="1"/>
      </svg>
      twlelectricalsoultions@mailpost-demo.com
    </p>

    <div class="social" aria-hidden="true">
      <span class="social__dot"></span>
      <span class="social__dot"></span>
    </div>
    <p class="handle">@twlelectricalsolutions</p>
  </section>
</main>
</body>
</html>
```